Business Card + Stationery Design for a Craft Beer Bar

Mr. Tolvek's is a taproom sport bar that contains in its menu beers from different places around the world. What we offer differently is the experience that you can get inside our location, ambient music with rock from the 80s to 90s, projection with the sports of the moment, board games and private events.

Target Market(s)

Young people, Mid and High Class

Industry/Entity Type

Business

Font styles to use
Serif
Sans Serif

Colors
fee18a

Requirements
Must have
• Name, Title, Contact Details, Website
Nice to have
• Mail Signature
Should not have
• n/a

```html
<!DOCTYPE html>
<html lang="en">
<head>
<meta charset="utf-8">
<title>Mr. Tolvek's Taproom — Business Card</title>
<link rel="stylesheet" href="https://fonts.googleapis.com/css2?family=Arimo:wght@400;700&display=swap">
<style>
  :root {
    --backdrop: #2b2b2b;
    --card: #f3c159;
    --ink: #1c1a17;
    --radius: 26px;
  }
  * { box-sizing: border-box; margin: 0; padding: 0; }
  html, body {
    width: 1200px;
    height: 880px;
    overflow: hidden;
    background: var(--backdrop);
    font-family: "Arimo", Arial, sans-serif;
    color: var(--ink);
  }
  .canvas { position: relative; width: 1200px; height: 880px; }
  .card {
    position: absolute;
    width: 580px;
    height: 332px;
    background: var(--card);
    border-radius: var(--radius);
  }

  /* Back of card */
  .card--back { left: 50px; top: 50px; }
  .card--back .brand-mark {
    position: absolute;
    left: 0; right: 0; top: 110px;
    display: flex; align-items: center; justify-content: center; gap: 12px;
  }
  .brand-mark__dot {
    width: 26px; height: 26px; border-radius: 50%; background: var(--ink);
  }
  .brand-mark__name {
    font-weight: 700; font-size: 30px; letter-spacing: 0.5px; text-transform: uppercase;
  }
  .card--back .website {
    position: absolute; left: 0; right: 0; top: 232px;
    text-align: center; font-size: 15px; letter-spacing: 1.5px;
  }

  /* Front of card */
  .card--front { left: 570px; top: 498px; }
  .holder { position: absolute; left: 36px; top: 40px; }
  .holder__name { font-weight: 700; font-size: 22px; }
  .holder__title { font-size: 16px; margin-top: 2px; }
  .card--front .brand-mark {
    position: absolute; right: 34px; top: 52px;
    display: flex; flex-direction: column; align-items: center; gap: 10px;
  }
  .card--front .brand-mark__name { font-size: 22px; text-align: center; line-height: 1.2; }
  .card--front .brand-mark__dot { width: 22px; height: 22px; }
  .address {
    position: absolute; right: 34px; top: 200px;
    text-align: right; font-size: 14px; line-height: 1.35;
  }
  .contacts {
    position: absolute; left: 36px; bottom: 30px;
    list-style: none; font-size: 14px;
  }
  .contacts li { display: flex; align-items: center; gap: 9px; margin-top: 5px; }
  .contacts svg { width: 18px; height: 18px; flex: none; }
</style>
</head>
<body>
<main class="canvas">

  <section class="card card--back" aria-label="Card back">
    <div class="brand-mark">
      <span class="brand-mark__dot"></span>
      <span class="brand-mark__name">Mr. Tolvek's</span>
    </div>
    <p class="website">www.tolvekstap.com</p>
  </section>

  <section class="card card--front" aria-label="Card front">
    <div class="holder">
      <p class="holder__name">Dario Kessel</p>
      <p class="holder__title">Owner</p>
    </div>

    <div class="brand-mark">
      <span class="brand-mark__dot"></span>
      <span class="brand-mark__name">Mr. Tolvek's<br>Taproom</span>
    </div>

    <p class="address">PO BOX 48 Harlan Road<br>7th street Millbrook,USA</p>

    <ul class="contacts">
      <li>
        <svg viewBox="0 0 20 20" aria-hidden="true"><circle cx="10" cy="10" r="9" fill="none" stroke="currentColor" stroke-width="1.4"/><rect x="7" y="5" width="6" height="10" rx="1" fill="none" stroke="currentColor" stroke-width="1.3"/></svg>
        (02) 4816 3570
      </li>
      <li>
        <svg viewBox="0 0 20 20" aria-hidden="true"><circle cx="10" cy="10" r="9" fill="none" stroke="currentColor" stroke-width="1.4"/><rect x="5.5" y="7" width="9" height="6.5" fill="none" stroke="currentColor" stroke-width="1.3"/><path d="M5.5 7 L10 11 L14.5 7" fill="none" stroke="currentColor" stroke-width="1.3"/></svg>
        hello@tolvekstap.com
      </li>
      <li>
        <svg viewBox="0 0 20 20" aria-hidden="true"><circle cx="10" cy="10" r="9" fill="none" stroke="currentColor" stroke-width="1.4"/><circle cx="10" cy="10" r="5" fill="none" stroke="currentColor" stroke-width="1.2"/><path d="M5 10 H15 M10 5 V15" stroke="currentColor" stroke-width="1.1"/></svg>
        www.tolvekstap.com
      </li>
    </ul>
  </section>

</main>
</body>
</html>
```